Sign Advertisment for Condominium Development

I need a sign created that will be placed in front of a building that is being converted into a luxury condominium development.

The sign needs to say:

Two, Boutique Luxury Condominiums Delivering late 2015.

Luxury Finishes // Designer Kitchens and Bath // Each Unit over 2,000 Square Feet

Deeded Parking Included with Each Unit

To Learn More, Contact:

Loretta Pinwell or Morgan Tesh
(202) 555-0147
Loretta.Pinwell@nrg-example.com

I need a small disclaimer at the bottom stating:

These Condominium(s) have not been registered by the Office of Residential Property Oversight Bureau of Dwelling Registration Tenancy Transfer and Purchase Section. A Condominium Unit may be reserved on a non-binding reservation agreement, but no contract of sale or lease that is binding on the purchaser may be entered into prior to registration.

Target Market(s)

Young professionals seeking luxury condominium

Industry/Entity Type

Building

Font styles to use
Serif

Colors
00a88f
ffffff

```html
<!DOCTYPE html>
<html lang="en">
<head>
<meta charset="utf-8">
<title>Two Boutique Luxury Condominiums – Delivering Late 2015</title>
<link rel="stylesheet" href="https://fonts.googleapis.com/css2?family=Tinos:ital,wght@0,400;1,400&display=swap">
<style>
  :root {
    --teal: #16a98d;
    --teal-deep: #0b7a66;
    --teal-mid: #3a9d8a;
    --teal-glow: #93d0c3;
    --white: #ffffff;
    --serif: "Tinos", "Times New Roman", serif;
  }
  html, body {
    margin: 0;
    padding: 0;
    width: 1200px;
    height: 800px;
    overflow: hidden;
    background: var(--teal);
  }
  .sign {
    position: relative;
    width: 1200px;
    height: 800px;
    background: var(--teal);
    color: var(--white);
    font-family: var(--serif);
    text-align: center;
  }
  .title-panel {
    position: absolute;
    left: 0;
    top: 0;
    width: 1200px;
    height: 480px;
  }
  .headline {
    position: absolute;
    left: 0;
    right: 0;
    top: 160px;
  }
  .headline__kicker {
    font-size: 45px;
    letter-spacing: 1px;
    line-height: 1;
    margin: 0;
  }
  .headline__kicker .dot { padding: 0 4px; vertical-align: 2px; }
  .headline__title {
    font-style: italic;
    font-size: 104px;
    line-height: 1;
    margin: 4px 0 0;
    font-weight: 400;
  }
  .headline__delivery {
    display: flex;
    justify-content: center;
    align-items: center;
    margin-top: 0;
    font-size: 33px;
    letter-spacing: 0.5px;
  }
  .rule {
    display: flex;
    align-items: center;
    width: 100px;
    height: 30px;
  }
  .rule::before, .rule::after { content: ""; display: block; }
  .rule--left::before, .rule--right::after {
    width: 5px; height: 5px; border-radius: 50%; background: var(--white); flex: none;
  }
  .rule--left::after, .rule--right::before {
    flex: 1; height: 1px; background: var(--white);
  }
  .rule--left { border-right: 1px solid var(--white); margin-right: 12px; }
  .rule--right { border-left: 1px solid var(--white); margin-left: 12px; }

  .features {
    position: absolute;
    left: 0;
    right: 0;
    top: 493px;
    font-size: 21.5px;
    letter-spacing: 0.3px;
    line-height: 33px;
  }
  .features p { margin: 0; }
  .sep { display: inline-block; width: 1px; height: 20px; background: rgba(255,255,255,0.7); margin: 0 14px; vertical-align: -3px; }

  .contact {
    position: absolute;
    left: 0;
    right: 0;
    top: 594px;
  }
  .contact__label { margin: 0; font-size: 17px; letter-spacing: 0.5px; }
  .contact__names { margin: 8px 0 0; font-size: 25px; letter-spacing: 0.5px; }
  .contact__names em { font-size: 23px; }
  .contact__lines { margin: 6px 0 0; font-size: 26px; }
  .contact__phone { font-size: 27px; }
  .contact__lines .sep { height: 10px; margin: 0 22px; vertical-align: 0; }
  .contact__email { font-style: italic; font-size: 24px; }

  .disclaimer {
    position: absolute;
    left: 30px;
    right: 30px;
    top: 721px;
    margin: 0;
    font-size: 13.5px;
    line-height: 21px;
  }
</style>
</head>
<body>
<main class="sign">
  <svg class="title-panel" viewBox="0 0 1200 480" role="img" aria-label="Decorative framed panel behind the headline">
    <defs>
      <radialGradient id="panel-glow" cx="600" cy="230" r="420" gradientUnits="userSpaceOnUse">
        <stop offset="0" stop-color="var(--teal-glow)"/>
        <stop offset="0.55" stop-color="var(--teal-mid)"/>
        <stop offset="1" stop-color="var(--teal-deep)"/>
      </radialGradient>
    </defs>
    <rect x="190" y="45" width="820" height="400" rx="200" ry="200"
          fill="url(#panel-glow)" stroke="var(--white)" stroke-width="10"/>
  </svg>

  <header class="headline">
    <p class="headline__kicker">TWO<span class="dot">·</span>BOUTIQUE<span class="dot">·</span>LUXURY</p>
    <h1 class="headline__title">Condominiums</h1>
    <div class="headline__delivery">
      <span class="rule rule--left"></span>
      <span>DELIVERING LATE 2015</span>
      <span class="rule rule--right"></span>
    </div>
  </header>

  <section class="features">
    <p>LUXURY FINISHES<span class="sep"></span>DESIGNER KITCHENS AND BATH</p>
    <p>EACH UNIT OVER 2,000 SQUARE FEET<span class="sep"></span>DEEDED PARKING INCLUDED WITH EACH UNIT</p>
  </section>

  <section class="contact">
    <p class="contact__label">TO LEARN MORE, CONTACT:</p>
    <p class="contact__names">LORETTA PINWELL <em>or</em> MORGAN TESH</p>
    <p class="contact__lines"><span class="contact__phone">(202) 555-0147</span><span class="sep"></span><span class="contact__email">Loretta.Pinwell@nrg-example.com</span></p>
  </section>

  <p class="disclaimer">These Condominium(s) have not been registered by the Office of Residential Property Oversight Bureau of Dwelling Registration Tenancy Transfer and Purchase Section.<br>A Condominium Unit may be reserved on a non-binding reservation agreement, but no contract of sale or lease that is binding on the purchaser may be entered into prior to registration.</p>
</main>
</body>
</html>
```